Product Line Brochure

Would like to have a bifold brochure for our product line to show to customers. Would like it to incorporate the paragraph description of the product line with the picture, followed by the product listings. I would like the brochure to be clean and modern. We are a specialty chemical manufacturer in NJ area.

```html
<!DOCTYPE html>
<html lang="en">
<head>
<meta charset="utf-8">
<title>Meridian Polymer, Inc. – Product Line Brochure</title>
<link href="https://fonts.googleapis.com/css2?family=Lato:wght@400;700;900&display=swap" rel="stylesheet">
<style>
  :root{
    --navy:#13305a;
    --navy-deep:#0b1f3d;
    --steel:#2f6f9a;
    --sky:#8fb3d6;
    --ink:#1b1b1b;
    --paper:#ffffff;
    --stage:#e4e5e7;
    --rock:#6f6a64;
    --rock-dark:#4c4844;
    --mist:#e9ecf0;
    --map-tone:#d9dde3;
  }
  *{box-sizing:border-box;margin:0;padding:0}
  html,body{width:1200px;height:900px;overflow:hidden}
  body{background:var(--stage);font-family:"Lato",sans-serif;color:var(--ink);position:relative}

  .panel{position:absolute;width:540px;height:360px;background:var(--paper);overflow:hidden;box-shadow:0 6px 18px rgba(0,0,0,.18)}

  /* Cover */
  .cover{left:330px;top:40px}
  .cover-photo{position:absolute;inset:0;background:
    linear-gradient(115deg,transparent 0 52%,rgba(11,31,61,.55) 52% 100%),
    linear-gradient(160deg,var(--sky) 0%,var(--steel) 45%,var(--navy-deep) 100%)}
  .cover-band{position:absolute;left:0;top:26px;width:330px;height:110px;background:var(--navy);clip-path:polygon(0 0,88% 0,100% 100%,0 100%)}
  .brand{position:absolute;left:40px;top:64px;display:flex;align-items:center;gap:10px;color:var(--paper);font-weight:700;font-size:18px;letter-spacing:.4px;text-transform:uppercase;white-space:nowrap}
  .brand-mark{width:13px;height:13px;background:var(--paper)}
  .cover-url{position:absolute;right:40px;bottom:22px;color:var(--paper);font-weight:700;font-size:13px}

  /* Inside spread */
  .inside-left{left:60px;top:480px}
  .inside-right{left:600px;top:480px;box-shadow:6px 6px 18px rgba(0,0,0,.18)}
  .spread-fold{position:absolute;left:600px;top:480px;width:14px;height:360px;background:linear-gradient(90deg,rgba(0,0,0,.10),rgba(0,0,0,0));z-index:2}

  .presence-band{position:absolute;left:0;top:0;width:100%;height:46px;background:var(--navy);color:var(--paper);font-weight:700;font-size:19px;padding:12px 24px;letter-spacing:.3px}
  .presence-map{position:absolute;left:18px;top:62px;width:320px;height:270px;
    background:radial-gradient(ellipse 62% 48% at 58% 42%,var(--map-tone) 0%,#e8ebef 55%,rgba(255,255,255,0) 100%),
               radial-gradient(ellipse 18% 14% at 16% 30%,#e3e6ea 0%,rgba(255,255,255,0) 100%)}
  .locations{position:absolute;left:350px;top:130px;list-style:none;font-size:11px;line-height:1.45}
  .locations li{display:flex;gap:8px;margin-bottom:18px}
  .locations svg{flex:none;margin-top:1px}

  .about-tab{position:absolute;left:16px;top:14px;background:var(--navy);color:var(--paper);font-weight:900;font-size:19px;padding:8px 34px 8px 22px;clip-path:polygon(0 0,100% 0,90% 100%,0 100%)}
  .about-copy{position:absolute;left:28px;top:66px;right:26px;font-size:11.5px;line-height:1.35;z-index:1}
  .about-copy p{margin-bottom:6px}
  .industries{list-style:disc;padding-left:16px}
  .about-photo{position:absolute;left:0;bottom:0;width:100%;height:190px;background:
    radial-gradient(ellipse 55% 70% at 62% 100%,var(--rock-dark) 0%,var(--rock) 45%,rgba(111,106,100,0) 100%),
    radial-gradient(ellipse 90% 55% at 50% 100%,#8d8780 0%,rgba(141,135,128,0) 100%),
    linear-gradient(180deg,rgba(255,255,255,0) 0%,var(--mist) 30%,#b9b4ad 70%,#9a948c 100%)}
</style>
</head>
<body>

<section class="panel cover">
  <div class="cover-photo" role="img" aria-label="Upward view of a modern glass office tower against a blue sky"></div>
  <div class="cover-band"></div>
  <div class="brand"><span class="brand-mark"></span>Meridian Polymer, Inc.</div>
  <div class="cover-url">www.meridianpolymer.com</div>
</section>

<section class="panel inside-left">
  <h2 class="presence-band">Meridian Polymer, Inc. - Our Presence</h2>
  <div class="presence-map" role="img" aria-label="Outline map of the United States with location pins in the Midwest, Southeast and New Jersey"></div>
  <ul class="locations">
    <li>
      <svg width="12" height="16" viewBox="0 0 12 16"><path d="M6 0a6 6 0 0 0-6 6c0 4.5 6 10 6 10s6-5.5 6-10a6 6 0 0 0-6-6z" fill="#3a6fc4"/><circle cx="6" cy="6" r="2.3" fill="#fff"/></svg>
      <span>MPI Headquarters<br>R&amp;D/Manufacturing/Sales<br>215 Harbor View Rd<br>Lyndhurst, NJ 07071</span>
    </li>
    <li>
      <svg width="12" height="16" viewBox="0 0 12 16"><path d="M6 0a6 6 0 0 0-6 6c0 4.5 6 10 6 10s6-5.5 6-10a6 6 0 0 0-6-6z" fill="#111"/><circle cx="6" cy="6" r="2.3" fill="#fff"/></svg>
      <span>IL - Technical Sales<br>MI - Technical Sales<br>NC - Technical Sales<br>GA - Technical Sales</span>
    </li>
  </ul>
</section>

<div class="spread-fold"></div>

<section class="panel inside-right">
  <div class="about-photo" role="img" aria-label="Soft-focus photo of a team of hikers climbing a rocky ridge"></div>
  <h2 class="about-tab">About Us</h2>
  <div class="about-copy">
    <p>Innovative specialty chemicals for almost 40 years. We combine a wealth of experience, with R&amp;D resources and the responsiveness of our technical and customer service team to support our customers.</p>
    <p>Industries including:</p>
    <ul class="industries">
      <li>Architectural</li>
      <li>Textiles &amp; Leather</li>
      <li>Inks, Paints &amp; Coatings</li>
      <li>Adhesives/Adhesion Promoters</li>
    </ul>
  </div>
</section>

</body>
</html>
```